Norwegian psychologist service needs a fresh and exiting web site*

Norwegian psychologist service: working with therapy, personal development, mastery and personal growth. Focus: children and teenagers with special needs; family dynamics; group processes; individuals with a need for therapy and personal growth. (Our company name: Fjordlys og samhold (means Mastery and Growth).

We already have a logo for the company, which will be used (will be attached in the project).

The webside is to be structured in 4 pages with roll down curtain menus (the numbers are just for guiding the designer - the should not be added):

Page 1: Om Fjordlys og Samhold (about Mastery and Growth): this is where our business is is presented/described shortly: Lorem Ipsum dolor cit...

Page 2: Tjenester (Services): this is where our 5 service areas are presented:
2.1 Utredning (Investigation, diagnosing): Lorem Ipsum dolor cit...
2.2 Rådgivning (consulting): Lorem Ipsum dolor cit...

2.3 Kurs og work shops (courses and work shops): Lorem Ipsum dolor cit...
2.3a Fjordlys og samhold Tema 1 (T1)
2.3b Fjordlys og samhold Tema 2 (T2)
2.3c Fjordlys og samhold Tema 3 (T3)

2.4 Terapi og utvikling (Therapy and development)
2.4a Fjordlys og samhold for individer (FS1)
2.4b Fjordlys og samhold i familier (FS2)
2.4c Fjordlys og samhold i grupper (FS3)
2.4d Fjordlys og samhold i institusjoner (FS4)

Page 3: Aktuelt (Blog): this is our blog where we share knowledge and articles

Page 4: Kontakt (Contact): This is the contact form page. Contact form should constitute:
- Ditt navn (your name)
- E-post (your e-mail)
- Emne (subject)
- Melding (message/description)

Our project should also include suggestion for handheld units (iPhone, iPad).
Updates

We have both been traveling with work for a while, and then unfortunately both of us got sick on return, so we need a few more days to evaluate and choose design. Kind Regards Arvid & Margit

Target Market(s)

Focus on therapy, learning, mastery and growth for children and teenagers with special needs, within the family dynamics, or in a group setting.
OUR MARKETS:
Private market: individuals, families, groups and health industry institutions (with focus on learning, mastery, growth (as well as growing up) and psychiatry for children and teenagers with special difficulties and needs)
Public institutions: Government institutions, state institutions and municipality institutions (e.g. schools, municipality health service, hospitals) that serve the public (families with children and teenagers with special needs, and where learning, mastery, growth (as well as growing up) and potential psychiatry is an issue).

Number of Pages Required

4 page

Font styles to use
Sans Serif

Colors

Designer to choose colors to be used in the design.

Requirements
Must have
• The website must have 4 pages with roll down curtain menus (we have added a PDF with suggested structure, and headings, with sub menus - see attached PDF drawing.
• The web page must also use the added logo file - and make the web page work well with our logo.
• We would like the website to have a modern look and we would like the site to be associated with typical HIGH END TOP QUALITY private health institutions, but with a stronger focus on human beings (hands, faces etc), and not white coats and doctors. We are psychologists in the private market.
• For instance, if photos are being used - we tend to like "warm" almost art-like, "grainy" two-tone (e.g. sepia) photos to illustrate our focus. If designer can find such photos as part of design, it would be interesting to us. We would like a few photos like that integrated in the design.
• We also want a design suggestion for how the web page should look like and behave on handheld units (e.g. iPhone, iPad).
Nice to have
• If designer could find a number of suitable photos that matches the business idea and design requirements (see description above), that could follow website, that would be good.
• It could also be nice to have graphic symbols that denote the different pages/subpages (subjects)....
• HORSES: we sometimes use horses as a "tool" in therapy sessions. The horse is not necessarily used for riding, but for contact, communication and grooming. PHOTOS: we would like the designer to find an opportunity for using a photo reflecting this cooperation between therapist, child, teenager and horse. It is a bit up to the designer to find a way to do this... Since the horse is only a tool, among many other tools, it does not have to be much - but we want to try and see how it will work with a photo that also reflects this part of our business.

```html
<!DOCTYPE html>
<html lang="no">
<head>
<meta charset="utf-8">
<title>Kontakt oss – Fjordlys og samhold</title>
<link href="https://fonts.googleapis.com/css2?family=IBM+Plex+Sans:wght@400;600;700&display=swap" rel="stylesheet">
<style>
  :root {
    --navy: #1e2178;
    --ink: #151515;
    --page-bg: #f4f1f1;
    --card: #ffffff;
    --field-border: #a9a9a9;
    --footer-bg: #131313;
    --footer-text: #ffffff;
    --muted: #9a9a9a;
    --rule: #3a3a3a;
    --social-1: #3b57a8;
    --social-2: #1e9be8;
    --social-3: #1c1d5c;
  }
  * { box-sizing: border-box; margin: 0; padding: 0; }
  html, body { width: 1167px; height: 1200px; overflow: hidden; }
  body {
    position: relative;
    font-family: "IBM Plex Sans", Arial, sans-serif;
    background: var(--page-bg);
    color: var(--ink);
  }
  .hero {
    position: absolute; left: 0; top: 0; width: 1167px; height: 517px;
    background:
      radial-gradient(ellipse at 55% 8%, rgba(255,250,235,0.95) 0%, rgba(255,245,225,0.6) 25%, rgba(255,240,220,0) 55%),
      linear-gradient(180deg, #f7f3ee 0%, #d9c7a9 14%, #8c6a3f 32%, #5a3f22 48%, #6e4b25 62%, #b8894c 78%, #d8b077 90%, #c89a5e 100%);
  }
  .brand {
    position: absolute; left: 131px; top: 60px;
    display: flex; align-items: center; gap: 10px;
    font-weight: 700; font-size: 24px; color: var(--navy); letter-spacing: 0.5px;
  }
  .brand-dot { width: 16px; height: 16px; border-radius: 50%; background: var(--navy); }
  .main-nav { position: absolute; top: 28px; left: 0; width: 1167px; height: 24px; }
  .main-nav a, .footer-nav a {
    position: absolute; text-decoration: none; font-weight: 600; font-size: 15.5px;
    white-space: nowrap; letter-spacing: 0.2px;
  }
  .main-nav a { color: var(--ink); }
  .main-nav a.is-active { color: var(--navy); }
  .nav-marker { position: absolute; left: 975px; top: 14px; }
  .page-title {
    position: absolute; top: 200px; left: 0; width: 1167px; text-align: center;
    color: #fff; font-weight: 700; font-size: 47px; letter-spacing: 1px;
    text-shadow: 0 2px 8px rgba(0,0,0,0.35);
  }
  .contact-card {
    position: absolute; left: 253px; top: 369px; width: 661px; height: 438px;
    background: var(--card); box-shadow: 0 6px 24px rgba(0,0,0,0.06);
  }
  .field {
    position: absolute; border: 2px solid var(--field-border); background: #fff;
    font-weight: 600; font-size: 12.5px; letter-spacing: 0.6px; color: #2a2a2a;
    padding-left: 16px; display: flex; align-items: center;
  }
  .field--name { left: 43px; top: 46px; width: 281px; height: 45px; }
  .field--email { left: 342px; top: 46px; width: 280px; height: 45px; }
  .field--subject { left: 43px; top: 113px; width: 579px; height: 45px; }
  .field--message { left: 43px; top: 178px; width: 579px; height: 139px; align-items: flex-start; padding-top: 14px; }
  .submit {
    position: absolute; left: 272px; top: 357px; width: 117px; height: 37px;
    background: var(--navy); color: #fff; border: none;
    font-family: inherit; font-weight: 600; font-size: 14.5px; letter-spacing: 0.6px;
  }
  .site-footer {
    position: absolute; left: 0; top: 901px; width: 1167px; height: 299px;
    background: var(--footer-bg); color: var(--footer-text);
  }
  .footer-brand {
    position: absolute; left: 131px; top: 110px;
    display: flex; align-items: center; gap: 10px;
    font-weight: 700; font-size: 24px; color: #fff;
  }
  .footer-brand .brand-dot { background: #fff; }
  .follow {
    position: absolute; left: 838px; top: 88px; font-weight: 600; font-size: 13px;
    letter-spacing: 0.5px; color: var(--muted);
  }
  .social { position: absolute; top: 83px; width: 30px; height: 30px; border-radius: 50%; }
  .social--a { left: 935px; background: var(--social-1); }
  .social--b { left: 973px; background: var(--social-2); }
  .social--c { left: 1011px; background: var(--social-3); }
  .footer-nav a { color: var(--footer-text); top: 142px; }
  .footer-rule { position: absolute; left: 566px; top: 189px; width: 473px; height: 1px; background: var(--rule); }
  .copyright { position: absolute; right: 128px; top: 217px; font-size: 11.5px; color: #d8d8d8; }
</style>
</head>
<body>
  <header class="hero" role="img" aria-label="Sunlit meadow with wild grasses and flowers at golden hour">
  </header>

  <div class="brand"><span class="brand-dot"></span>Fjordlys og samhold</div>

  <nav class="main-nav">
    <a href="#" style="left:643px">OM OSS</a>
    <a href="#" style="left:733px">TJENESTER</a>
    <a href="#" style="left:851px">AKTUELT</a>
    <a href="#" class="is-active" style="left:938px">KONTAKT OSS</a>
  </nav>
  <svg class="nav-marker" width="10" height="14" viewBox="0 0 10 14" aria-hidden="true">
    <path d="M5 0 C8 5 10 8 10 10 A5 4 0 0 1 0 10 C0 8 2 5 5 0 Z" fill="#1e2178"/>
  </svg>

  <h1 class="page-title">KONTAKT OSS</h1>

  <form class="contact-card">
    <div class="field field--name">DITT NAVN</div>
    <div class="field field--email">E-POST</div>
    <div class="field field--subject">EMNE</div>
    <div class="field field--message">MELDING</div>
    <button class="submit" type="button">SENDE INN</button>
  </form>

  <footer class="site-footer">
    <div class="footer-brand"><span class="brand-dot"></span>Fjordlys og samhold</div>
    <span class="follow">FOLLOW US</span>
    <span class="social social--a"></span>
    <span class="social social--b"></span>
    <span class="social social--c"></span>
    <nav class="footer-nav">
      <a href="#" style="left:568px">HJEM</a>
      <a href="#" style="left:641px">OM OSS</a>
      <a href="#" style="left:731px">TJENESTER</a>
      <a href="#" style="left:850px">AKTUELT</a>
      <a href="#" style="left:936px">KONTAKT OSS</a>
    </nav>
    <div class="footer-rule"></div>
    <p class="copyright">Copyright © 2020 All Rights Reserved</p>
  </footer>
</body>
</html>
```